MRC New Busines Card

we need a business card for or renovation company, our main color is orange and our logo is a concrete ball rolling with MRC on it.the company name is Maple Ridge Contractors, Inc, we need somthing simple but profecional, also that we can change if its for roofing or renovations and the names

Target Market(s)

home owners

Industry/Entity Type

Concrete

Contact Information for Business Card

.

Colors
f68d4d
f9ba93
f37122
f78f20
faa54b
fbc994

```html
<!DOCTYPE html>
<html lang="en">
<head>
<meta charset="utf-8">
<title>Maple Ridge Contractors – Business Card</title>
<link href="https://fonts.googleapis.com/css2?family=Arimo:wght@400;700&display=swap" rel="stylesheet">
<style>
  :root{
    --orange-deep:#e0691c;
    --orange:#f37122;
    --orange-mid:#f78f20;
    --orange-light:#faa54b;
    --ink:#161616;
    --grey-text:#2a2a2a;
    --card:#ffffff;
    --card-shade:#eeeeee;
    --backdrop:#e9e6e1;
  }
  *{margin:0;padding:0;box-sizing:border-box}
  html,body{width:1200px;height:892px;overflow:hidden}
  body{background:var(--backdrop);font-family:"Arimo",Arial,sans-serif;position:relative}
  .card{position:absolute;left:100px;top:156px;width:1000px;height:580px;
    background:linear-gradient(135deg,var(--card) 40%,var(--card-shade));
    box-shadow:0 10px 30px rgba(0,0,0,.18);overflow:hidden}
  .band{position:absolute;left:0;width:100%}
  .band--top{top:0;height:70px;background:linear-gradient(90deg,var(--orange-deep),var(--orange-mid) 60%,var(--orange-light));
    border-bottom:3px solid var(--ink)}
  .band--bottom{bottom:0;height:110px;background:linear-gradient(90deg,var(--orange-light),var(--orange-mid) 45%,var(--orange-deep));
    border-top:3px solid var(--ink)}
  .band-dashes{position:absolute;right:60px;top:80px;display:flex;gap:12px}
  .band-dashes span{width:14px;height:5px;background:var(--orange)}
  .name-square{position:absolute;left:40px;top:380px;width:150px;height:150px;background:var(--card);
    border:3px solid var(--ink)}
  .company{position:absolute;left:214px;top:350px;font-weight:700;font-size:26px;line-height:30px;color:var(--ink)}
  .phone-main{position:absolute;left:214px;top:412px;font-size:26px;line-height:30px;color:var(--orange)}
  .contacts{position:absolute;left:214px;top:366px;list-style:none;font-size:15px;line-height:19px;color:var(--grey-text);display:none}
  .details{position:absolute;left:230px;top:262px;list-style:none;font-size:15px;line-height:19px;color:var(--grey-text)}
  .details .accent{color:var(--orange)}
  .services{position:absolute;right:60px;top:110px;text-align:right;font-weight:700;font-size:22px;line-height:26px;color:var(--orange-mid)}
  .brand-name{position:absolute;left:600px;top:112px;font-weight:700;font-size:34px;line-height:40px;color:var(--ink)}
  .tagline{position:absolute;left:560px;top:384px;width:390px;height:60px;border:2px solid var(--orange);
    display:flex;align-items:center;justify-content:center;font-size:17px;color:var(--ink)}
</style>
</head>
<body>
  <article class="card">
    <div class="band band--top"></div>
    <div class="band-dashes"><span></span><span></span><span></span></div>

    <span class="brand-name">MRC</span>

    <div class="services">Roofing<br>Painting<br>Renovations</div>

    <ul class="details">
      <li>(555)-310-4827</li>
      <li>www.<span class="accent">mapleridgecontractors</span>.com</li>
      <li>info@<span class="accent">MapleRidgeContractors</span>.com</li>
      <li>418 Cedar Hollow Rd Fairview, GA 30099</li>
    </ul>

    <div class="tagline">“Taking The Service Industry To The Next Level”</div>

    <div class="band band--bottom"></div>
    <div class="name-square"></div>
    <h1 class="company">Maple Ridge Contractors, Inc</h1>
    <p class="phone-main">(555)-318-2064</p>
  </article>
</body>
</html>
```